TITLE: What Makes My Child’s Playing Talent Grow? SUB-TITLE: A Mother’s Plain Talk Manual for Coaching...

My book is for parents who have young children that are really into sports. My book empowers parents so they can motivate their children to succeed. It deals with sports psychology. Both my title and subtitle should be easy to read. Ideally, I would like a picture of young athlete(s) on the title. I have uploaded files of some books on Brindlemart that deal with the same subject. The last two files are 1) my company logo, please try to include these colors 2) an ebook cover I put together myself. You will notice an On-line bonus in the middle of the book, this Bonus needs to be on the cover.

Target Market(s)

Parents with children who play sports at a high level

Colors

Designer to choose colors to be used in the design.

Requirements
Must have
• Online Bonus feature as per my example.
• Dimensions: Pagelux = The ideal size of your eBook cover art is a height/width ratio of 1.6:1. This means that for every 1,000 pixels in width, the image should be 1,600 pixels in height.
Nice to have
• picture of a young athlete or young athletes

```html
<!DOCTYPE html>
<html lang="en">
<head>
<meta charset="utf-8">
<title>What Makes My Child’s Playing Talent Grow? – Cover</title>
<link href="https://fonts.googleapis.com/css2?family=Montserrat:wght@300;600;700;800;900&display=swap" rel="stylesheet">
<style>
  :root {
    --backdrop: #a3a3a3;
    --paper: #ffffff;
    --ink-dark: #3d3a35;
    --ink-grey: #5d676b;
    --accent-orange: #f07f1e;
    --accent-orange-deep: #d9620f;
    --badge-light: #f6a040;
    --on-dark: #ffffff;
  }
  html, body {
    margin: 0;
    width: 1200px;
    height: 1200px;
    overflow: hidden;
    background: var(--backdrop);
    font-family: "Montserrat", Arial, sans-serif;
  }
  .book-cover {
    position: absolute;
    left: 270px;
    top: 72px;
    width: 660px;
    height: 1056px;
    display: block;
  }
  .cover-paper { fill: var(--paper); }
  .title-lead { font-weight: 300; fill: var(--ink-grey); font-size: 32px; }
  .title-main { font-weight: 900; fill: var(--ink-dark); font-size: 112px; }
  .title-accent { font-weight: 800; fill: var(--accent-orange); font-size: 42px; }
  .bonus-burst { fill: var(--accent-orange); }
  .bonus-ring { fill: var(--paper); }
  .bonus-core { fill: url(#bonusGlow); }
  .bonus-text { fill: var(--ink-dark); text-anchor: middle; font-weight: 700; }
  .bonus-price { font-weight: 800; }
  .subtitle-band { fill: var(--ink-dark); }
  .subtitle-fold { fill: #24221f; }
  .subtitle-text { fill: var(--on-dark); font-weight: 800; }
  .brand-disc { fill: var(--accent-orange); }
  .brand-name { fill: var(--on-dark); font-weight: 700; font-size: 17px; text-anchor: middle; letter-spacing: 1px; }
</style>
</head>
<body>
<svg class="book-cover" viewBox="0 0 589 942" xmlns="http://www.w3.org/2000/svg">
  <defs>
    <radialGradient id="bonusGlow" cx="0.45" cy="0.4" r="0.65">
      <stop offset="0" stop-color="var(--badge-light)"/>
      <stop offset="1" stop-color="var(--accent-orange-deep)"/>
    </radialGradient>
    <linearGradient id="athleteTones" x1="0" y1="0" x2="1" y2="1">
      <stop offset="0" stop-color="#c99a66"/>
      <stop offset="0.45" stop-color="#e9e6e0"/>
      <stop offset="0.8" stop-color="#3f8a4c"/>
      <stop offset="1" stop-color="#f2f2f2"/>
    </linearGradient>
  </defs>

  <rect class="cover-paper" width="589" height="942"/>

  <g class="cover-title">
    <text class="title-lead" x="62" y="92" textLength="468" lengthAdjust="spacingAndGlyphs">WHAT MAKES MY</text>
    <text class="title-main" x="62" y="193" textLength="466" lengthAdjust="spacingAndGlyphs">CHILD’S</text>
    <text class="title-accent" x="64" y="240" textLength="462" lengthAdjust="spacingAndGlyphs">PLAYING TALENT GROW?</text>
  </g>

  <rect class="athlete-photo" role="img" aria-label="Photo of a young cross-country runner in a white and green singlet, running in profile"
        x="137" y="300" width="262" height="460" rx="40" fill="url(#athleteTones)" opacity="0.85"/>

  <g class="bonus-badge">
    <polygon class="bonus-burst" points="436,265 444,277 455,268 460,282 473,277 473,291 487,291 482,304 496,309 487,320 498,329 486,336 495,348 481,351 485,365 471,364 471,378 458,373 453,387 442,378 436,391 430,378 419,387 414,373 401,378 401,364 387,365 391,351 377,348 386,336 374,329 385,320 376,309 390,304 385,291 399,291 399,277 412,282 417,268 428,277"/>
    <circle class="bonus-ring" cx="436" cy="328" r="56"/>
    <circle class="bonus-core" cx="436" cy="328" r="52"/>
    <text class="bonus-text" x="436" y="313" font-size="17">FREE</text>
    <text class="bonus-text" x="436" y="321" font-size="7">ONLINE</text>
    <text class="bonus-text" x="436" y="328" font-size="7">WORKSHOP</text>
    <text class="bonus-text bonus-price" x="436" y="356" font-size="30">$170</text>
    <text class="bonus-text" x="438" y="371" font-size="15">VALUE</text>
    <text class="bonus-text" x="436" y="381" font-size="5">Details Inside</text>
  </g>

  <g class="subtitle-banner">
    <polygon class="subtitle-fold" points="90,830 122,819 125,880"/>
    <polygon class="subtitle-band" points="108,812 500,733 515,802 125,880"/>
    <g transform="rotate(-11.5 300 810)">
      <text class="subtitle-text" x="180" y="790" font-size="21" textLength="250" lengthAdjust="spacingAndGlyphs">A MOTHER’S PLAIN TALK</text>
      <text class="subtitle-text" x="138" y="825" font-size="29" textLength="340" lengthAdjust="spacingAndGlyphs">MANUAL FOR COACHING...</text>
    </g>
  </g>

  <g class="publisher-brand">
    <circle class="brand-disc" cx="133" cy="737" r="70"/>
    <text class="brand-name" x="133" y="732">FOCUS</text>
    <text class="brand-name" x="133" y="753">FIELD</text>
  </g>
</svg>
</body>
</html>
```